Specialist Medical practice after professional trifold flyer design for patient information brochure

I am the Director of the Hollowbrook Clinic, a specialist medial and surgical practice in Australia. I am after a professional design of a patient information trifold flyer that can be used for web distribution or for commercial printing for upcoming educational event. The design would need to allow change of images and text to be used as template for future topics but have a common brand look across them. Colours would follow the logo, but primarily blue colours for the hollowbrook theme. The inside text needs to be clearly contrasted to the background for easy reading, as often elderly patients. The design would make use of curves or circles, but open for hexagonal, triangle square vector components. I have included an outline for the initial brochure and included images to include. Other stock background images can be used if they increase the impact of the design over included. A winning design is also one that could be modified to a 4 page bi-fold brochure

Target Market(s)

This will be provided to patients in GP practices, podiatry clinics, radiological practices. Aimed at patients to read and be compelled to look to site or get consultation with me

Industry/Entity Type

Medical

Font styles to use
Serif
Sans Serif

Colors
33a6d7
0355a3
86cfc6
cedeed
0292cd
85cae6

Requirements
Must have
• The front cover needs to engage the patient to pick up and read- yes I have a painful ankle and want to find out more. the goal for the inside is to provide the options but be able to direct to website for more info - website currently undergoing upgrade. After professional modern look. Not bright contrasting colours like many advertising brochures. Needs to able to have images and text changed but following same look to create new topics
Nice to have
• The focus is a Tri-fold brochure. Nice to be able to modify to bifold. A winning design would even offer both, or submit separate bifold and trifold. I am open to different versions of similar look. (eg option of brochure with curved elements, triangular or square, or hexagonal.
Should not have
• To many contrasting colours. Text must be easily read on background, either white or coloured background texture with transparency

```html
<!DOCTYPE html>
<html lang="en">
<head>
<meta charset="utf-8">
<title>My Painful Ankle – Trifold Brochure</title>
<link href="https://fonts.googleapis.com/css2?family=Roboto:wght@400;500;700&family=Roboto+Condensed:wght@300;400&display=swap" rel="stylesheet">
<style>
  :root{
    --backdrop:#7e7e7e;
    --paper:#ffffff;
    --blue-deep:#1f55a3;
    --blue-panel:#3a78be;
    --blue-panel-dark:#2d64ad;
    --teal:#3cbcaa;
    --teal-light:#86cfc6;
    --ink:#3b3b3b;
    --white:#ffffff;
  }
  *{box-sizing:border-box;margin:0;padding:0}
  html,body{width:837px;height:1200px;overflow:hidden}
  body{background:var(--backdrop);font-family:"Roboto",Arial,sans-serif;color:var(--ink);position:relative}
  .brochure{position:absolute;left:18px;top:290px;width:800px;height:621px;background:var(--paper);
    box-shadow:0 18px 30px rgba(0,0,0,.35);overflow:hidden}
  .artwork{position:absolute;inset:0}
  .panel-divider{position:absolute;top:0;bottom:0;width:1px;background:rgba(0,0,0,.06)}

  /* left panel */
  .bio{position:absolute;left:10px;width:241px;color:var(--white);text-align:center}
  .bio-name{top:262px;font-size:17px;font-weight:500;letter-spacing:.2px}
  .bio-creds{top:285px;font-size:7.5px}
  .bio-text{top:304px;font-size:8.6px;line-height:12px;text-align:center;padding:0 14px}
  .conditions-title{position:absolute;top:400px;left:0;width:261px;text-align:center;color:var(--white);
    font-size:13.5px;font-weight:500;font-variant:small-caps;letter-spacing:.3px}
  .conditions-intro{position:absolute;top:427px;left:12px;width:240px;color:var(--white);font-size:7.4px;line-height:10.5px}
  .conditions-list{position:absolute;top:459px;left:12px;width:240px;list-style:none}
  .conditions-list li{display:flex;gap:4px;color:var(--white);font-size:7.4px;line-height:10.8px;
    padding:3px 0 6px;border-bottom:1px solid rgba(255,255,255,.45);margin-bottom:4px}
  .conditions-list svg{flex:0 0 8px;margin-top:1px}

  /* middle panel */
  .contact{position:absolute;left:271px;width:245px;text-align:center}
  .contact-title{top:399px;font-family:"Roboto Condensed",sans-serif;font-weight:300;font-size:22px;letter-spacing:.5px;color:var(--ink)}
  .contact-lines{top:433px;font-size:10.4px;line-height:17.3px;color:var(--ink)}
  .contact-lines svg{vertical-align:-1px;margin-right:4px}

  /* brand mark */
  .brand{position:absolute;display:flex;align-items:center;gap:5px;top:578px;height:22px}
  .brand-dot{width:14px;height:14px;border-radius:50%;border:2px solid var(--blue-deep)}
  .brand-name{font-size:11.5px;font-weight:700;color:var(--blue-deep);letter-spacing:.4px;text-transform:uppercase}
  .brand--middle{left:333px}
  .brand--cover{left:600px}

  /* cover */
  .cover-title{position:absolute;top:462px;left:530px;width:270px;text-align:center;color:var(--blue-deep);
    font-size:22px;font-weight:700;letter-spacing:.2px}
  .cover-sub{position:absolute;top:490px;left:530px;width:270px;text-align:center;color:var(--teal);
    font-size:9.4px;font-weight:500;letter-spacing:.3px}
  .cover-pill{position:absolute;top:516px;left:552px;width:221px;height:42px;border-radius:12px;
    background:var(--teal);color:var(--white);text-align:center;padding-top:6px;box-shadow:0 2px 4px rgba(0,0,0,.15)}
  .cover-pill-name{font-size:13px;font-weight:500;letter-spacing:.3px}
  .cover-pill-role{font-size:8.2px;letter-spacing:.2px}
</style>
</head>
<body>
<main class="brochure">
  <svg class="artwork" viewBox="0 0 800 621" width="800" height="621">
    <defs>
      <linearGradient id="runnerTones" x1="0" y1="0" x2="1" y2="1">
        <stop offset="0" stop-color="#e9d9b8"/>
        <stop offset=".45" stop-color="#c79a66"/>
        <stop offset="1" stop-color="#8c7440"/>
      </linearGradient>
      <linearGradient id="buildingTones" x1="0" y1="0" x2="0" y2="1">
        <stop offset="0" stop-color="#7fa3c8"/>
        <stop offset=".6" stop-color="#d9dde2"/>
        <stop offset="1" stop-color="#4f5a3a"/>
      </linearGradient>
      <linearGradient id="portraitTones" x1="0" y1="0" x2="0" y2="1">
        <stop offset="0" stop-color="#f3f3f3"/>
        <stop offset=".5" stop-color="#d9c2b0"/>
        <stop offset="1" stop-color="#2a2a30"/>
      </linearGradient>
      <linearGradient id="panelBlue" x1="0" y1="0" x2="0" y2="1">
        <stop offset="0" stop-color="var(--blue-panel)"/>
        <stop offset="1" stop-color="var(--blue-panel-dark)"/>
      </linearGradient>
      <filter id="ringShadow" x="-20%" y="-20%" width="140%" height="140%">
        <feDropShadow dx="0" dy="2" stdDeviation="3" flood-opacity=".3"/>
      </filter>
    </defs>

    <!-- left panel -->
    <rect x="58" y="26" width="150" height="200" fill="url(#portraitTones)" role="img" aria-label="Portrait photograph of the surgeon in a dark suit"/>
    <path d="M0,228 C90,208 170,204 261,244 L261,621 L0,621 Z" fill="var(--teal)"/>
    <path d="M0,244 C90,226 170,222 261,260 L261,621 L0,621 Z" fill="url(#panelBlue)"/>

    <!-- cover / inside photograph -->
    <path d="M261,0 H800 V388 C660,384 530,350 430,296 C370,264 310,252 261,254 Z" fill="url(#runnerTones)" role="img" aria-label="Photograph of a runner holding a sore ankle outdoors at sunset"/>
    <path d="M455,318 C580,382 690,394 800,392 L800,408 C680,410 560,390 455,318 Z" fill="var(--teal)"/>
    <path d="M500,346 C610,404 710,414 800,412 V436 C700,434 590,414 500,346 Z" fill="var(--blue-deep)"/>

    <!-- building circle -->
    <circle cx="394" cy="280" r="104" fill="#ffffff" filter="url(#ringShadow)"/>
    <circle cx="394" cy="280" r="96" fill="url(#buildingTones)" role="img" aria-label="Photograph of the private hospital building"/>
  </svg>

  <div class="panel-divider" style="left:261px"></div>
  <div class="panel-divider" style="left:526px"></div>

  <!-- left panel text -->
  <h2 class="bio bio-name">DR MARTIN HALE</h2>
  <p class="bio bio-creds">MBBS (Hons), FRACS (Ortho), FA (Ortho)</p>
  <p class="bio bio-text">Dr Martin Hale is an Australian trained Orthopaedic Surgeon who has a primary focus in the treatment of conditions of the foot and ankle. He has completed post fellowship training in Foot and Ankle surgery both locally and internationally, and continues to update himself in the latest techniques.</p>

  <h3 class="conditions-title">Conditions Treated</h3>
  <p class="conditions-intro">Dr Hale provides assessment and treatment of all foot and ankle conditions. He has special interest in the following.</p>
  <ul class="conditions-list">
    <li><svg width="8" height="8" viewBox="0 0 8 8"><circle cx="4" cy="4" r="3.4" fill="none" stroke="#fff" stroke-width=".8"/><path d="M2.3,4.1 3.5,5.2 5.8,2.8" fill="none" stroke="#fff" stroke-width=".8"/></svg>Minimally invasive treatment for bunions and toe deformities.</li>
    <li><svg width="8" height="8" viewBox="0 0 8 8"><circle cx="4" cy="4" r="3.4" fill="none" stroke="#fff" stroke-width=".8"/><path d="M2.3,4.1 3.5,5.2 5.8,2.8" fill="none" stroke="#fff" stroke-width=".8"/></svg>Joint sparing procedures for arthritis or deformity, including a synthetic cartilage implant.</li>
    <li><svg width="8" height="8" viewBox="0 0 8 8"><circle cx="4" cy="4" r="3.4" fill="none" stroke="#fff" stroke-width=".8"/><path d="M2.3,4.1 3.5,5.2 5.8,2.8" fill="none" stroke="#fff" stroke-width=".8"/></svg>Joint fusion procedures for arthritis of the feet and ankle.</li>
    <li><svg width="8" height="8" viewBox="0 0 8 8"><circle cx="4" cy="4" r="3.4" fill="none" stroke="#fff" stroke-width=".8"/><path d="M2.3,4.1 3.5,5.2 5.8,2.8" fill="none" stroke="#fff" stroke-width=".8"/></svg>Sports injuries and tendinopathies.</li>
    <li><svg width="8" height="8" viewBox="0 0 8 8"><circle cx="4" cy="4" r="3.4" fill="none" stroke="#fff" stroke-width=".8"/><path d="M2.3,4.1 3.5,5.2 5.8,2.8" fill="none" stroke="#fff" stroke-width=".8"/></svg>Total ankle replacement and deformity correction of the foot and ankle.</li>
  </ul>

  <!-- middle panel text -->
  <h2 class="contact contact-title">CONTACT US</h2>
  <div class="contact contact-lines">
    <div><svg width="7" height="9" viewBox="0 0 7 9"><path d="M3.5,0 C1.5,0 0,1.5 0,3.4 C0,5.8 3.5,9 3.5,9 C3.5,9 7,5.8 7,3.4 C7,1.5 5.5,0 3.5,0 Z" fill="var(--blue-deep)"/><circle cx="3.5" cy="3.4" r="1.2" fill="#fff"/></svg>Suite 412, Level 4</div>
    <div>Harbourside Private Hospital</div>
    <div>218-222 Marine St Kestrel Bay NSW</div>
    <div><svg width="7" height="9" viewBox="0 0 7 9"><path d="M3.5,0 C1.5,0 0,1.5 0,3.4 C0,5.8 3.5,9 3.5,9 C3.5,9 7,5.8 7,3.4 C7,1.5 5.5,0 3.5,0 Z" fill="var(--blue-deep)"/><circle cx="3.5" cy="3.4" r="1.2" fill="#fff"/></svg>45 Ferry Road Linden NSW</div>
    <div><svg width="8" height="8" viewBox="0 0 8 8"><path d="M1.5,0.5 L3,0.5 L3.6,2.4 L2.6,3.2 C3.1,4.3 3.8,5 4.8,5.4 L5.6,4.4 L7.5,5 L7.5,6.5 C7.5,7.1 7,7.5 6.4,7.5 C3.2,7.3 0.7,4.8 0.5,1.6 C0.5,1 0.9,0.5 1.5,0.5 Z" fill="var(--blue-deep)"/></svg>(02) 5550 1234</div>
    <div><svg width="9" height="8" viewBox="0 0 9 8"><rect x="2" y="0" width="5" height="2.5" fill="var(--blue-deep)"/><rect x="0" y="2.5" width="9" height="4" rx="1" fill="var(--blue-deep)"/><rect x="2" y="5" width="5" height="3" fill="var(--blue-deep)"/></svg>(02) 5550 1288</div>
    <div><svg width="9" height="7" viewBox="0 0 9 7"><rect x="0" y="0" width="9" height="7" rx="1" fill="var(--blue-deep)"/><path d="M0.5,0.8 4.5,4 8.5,0.8" fill="none" stroke="#fff" stroke-width=".8"/></svg>info@hollowbrookclinic.com.au</div>
    <div><svg width="8" height="8" viewBox="0 0 8 8"><circle cx="4" cy="4" r="3.5" fill="none" stroke="var(--blue-deep)" stroke-width=".9"/><ellipse cx="4" cy="4" rx="1.5" ry="3.5" fill="none" stroke="var(--blue-deep)" stroke-width=".7"/><path d="M0.5,4 H7.5" stroke="var(--blue-deep)" stroke-width=".7"/></svg>www.hollowbrookclinic.com.au</div>
  </div>
  <div class="brand brand--middle"><span class="brand-dot"></span><span class="brand-name">Hollowbrook Clinic</span></div>

  <!-- cover text -->
  <h1 class="cover-title">MY PAINFUL ANKLE</h1>
  <p class="cover-sub">SOLUTIONS FOR ANKLE ARTHRITIS</p>
  <div class="cover-pill">
    <div class="cover-pill-name">DR MARTIN HALE</div>
    <div class="cover-pill-role">ORTHOPAEDIC FOOT AND ANKLE SURGEON</div>
  </div>
  <div class="brand brand--cover"><span class="brand-dot"></span><span class="brand-name">Hollowbrook Clinic</span></div>
</main>
</body>
</html>
```